TAILWIND FIELDS Pet Resorts Outdoor Signage

4 x 8 outdoor signage design for our two locations

Target Market(s)

Existing and New Customers

Industry/Entity Type

Pet Care

Font styles to use
Sans Serif

Colors

Designer to choose colors to be used in the design.

```html
<!DOCTYPE html>
<html lang="en">
<head>
<meta charset="utf-8">
<title>TAILWIND FIELDS Pet Resorts – Outdoor Signage</title>
<link rel="stylesheet" href="https://fonts.googleapis.com/css2?family=Open+Sans:wght@600;700;800&display=swap">
<style>
  :root {
    --backdrop: #cccccc;
    --sign-white: #ffffff;
    --charcoal: #474747;
    --steel-teal: #4a8fa6;
    --steel-teal-deep: #3a6577;
    --club-teal: #20a9a8;
    --club-teal-dark: #1d9a99;
  }
  * { margin: 0; padding: 0; box-sizing: border-box; }
  html, body {
    width: 1200px; height: 1114px; overflow: hidden;
    background: var(--backdrop);
    font-family: "Open Sans", Arial, sans-serif;
  }
  .sign {
    position: absolute; width: 873px; height: 437px;
    background: var(--sign-white); overflow: hidden;
  }
  .sign--resort { left: 163px; top: 98px; }
  .sign--club { left: 168px; top: 569px; }
  .sign__shapes { position: absolute; inset: 0; }
  .sign__text { position: absolute; white-space: nowrap; line-height: 1; }

  /* Resort sign */
  .services-strip {
    left: 48px; right: 0; top: 9px; text-align: center;
    color: var(--sign-white); font-weight: 700; font-size: 21px; letter-spacing: -0.2px;
    padding-left: 55px;
  }
  .brand {
    display: flex; align-items: center; justify-content: center; gap: 12px;
    font-weight: 800; letter-spacing: 0.5px;
  }
  .brand__mark { width: 22px; height: 22px; border-radius: 50%; background: var(--steel-teal); flex: none; }
  .brand--resort { left: 0; right: 0; top: 122px; font-size: 40px; color: var(--charcoal); }
  .services-main {
    left: 0; right: 0; top: 218px; text-align: center;
    color: var(--steel-teal); font-weight: 700; font-size: 43px; letter-spacing: -0.4px;
  }
  .breed-note {
    left: 0; right: 0; top: 263px; text-align: center;
    color: var(--charcoal); font-weight: 700; font-size: 28px; letter-spacing: -0.3px;
  }
  .resort-label {
    left: 27px; top: 363px; color: var(--sign-white);
    font-weight: 700; font-size: 58px; letter-spacing: -0.5px;
  }
  .resort-phone {
    left: 495px; width: 280px; top: 368px; text-align: center;
    color: var(--sign-white); font-weight: 700; font-size: 35px;
  }
  .resort-web {
    left: 475px; width: 320px; top: 404px; text-align: center;
    color: var(--steel-teal); font-weight: 800; font-size: 23px;
  }

  /* Club sign */
  .club-phone {
    left: 330px; width: 490px; top: 17px; text-align: center;
    color: var(--sign-white); font-weight: 800; font-size: 56px; letter-spacing: 1px;
  }
  .brand--club {
    left: 22px; top: 196px; flex-direction: column; align-items: flex-start; gap: 8px;
    font-size: 34px; color: var(--charcoal); line-height: 0.95;
  }
  .brand--club .brand__mark { border-radius: 0; width: 26px; height: 26px; background: var(--club-teal); }
  .campus-title {
    left: 213px; top: 186px; color: var(--charcoal);
    font-weight: 800; font-size: 40px; letter-spacing: -0.6px;
  }
  .campus-tagline {
    left: 213px; top: 228px; color: var(--club-teal);
    font-weight: 800; font-size: 40px; letter-spacing: -0.6px;
  }
  .club-web {
    left: 120px; width: 390px; top: 384px; text-align: center;
    color: var(--sign-white); font-weight: 800; font-size: 36px;
  }
</style>
</head>
<body>

<section class="sign sign--resort" aria-label="Pet resort sign">
  <svg class="sign__shapes" viewBox="0 0 873 437" width="873" height="437" aria-hidden="true">
    <defs>
      <linearGradient id="resortBand" x1="0" y1="0" x2="1" y2="0">
        <stop offset="0" stop-color="#4a8fa6"/>
        <stop offset="1" stop-color="#3a6577"/>
      </linearGradient>
    </defs>
    <path d="M48 0 H873 V37 H108 C82 37 66 18 48 0 Z" fill="var(--steel-teal)"/>
    <path d="M395 363 H833 C852 363 862 380 873 405 V437 H395 Z" fill="var(--charcoal)"/>
    <path d="M0 337 H361 C385 337 398 346 412 365 L461 437 H0 Z" fill="url(#resortBand)"/>
  </svg>
  <p class="sign__text services-strip">FULL-SERVICE SALON – PET TAXI &amp; MORE</p>
  <div class="sign__text brand brand--resort"><span class="brand__mark"></span>TAILWIND FIELDS</div>
  <h1 class="sign__text services-main">BOARDING – DAYCARE – TRAINING</h1>
  <p class="sign__text breed-note">ALL BREED FRIENDLY</p>
  <p class="sign__text resort-label">PET RESORT</p>
  <p class="sign__text resort-phone">905-555-0142</p>
  <p class="sign__text resort-web">WWW.TAILWINDFIELDS.CA</p>
</section>

<section class="sign sign--club" aria-label="Social club campus sign">
  <svg class="sign__shapes" viewBox="0 0 873 437" width="873" height="437" aria-hidden="true">
    <path d="M15 0 H260 V47 H50 C34 47 24 30 15 0 Z" fill="var(--charcoal)"/>
    <path d="M232 0 H873 V93 H318 C300 93 290 85 280 70 Z" fill="var(--club-teal)"/>
    <path d="M650 391 H840 C856 391 864 408 873 437 H672 Z" fill="var(--club-teal)"/>
    <path d="M0 370 H616 C640 370 652 388 677 437 H0 Z" fill="var(--charcoal)"/>
  </svg>
  <p class="sign__text club-phone">437-555-0178</p>
  <div class="sign__text brand brand--club"><span class="brand__mark"></span>TAILWIND<br>FIELDS</div>
  <h2 class="sign__text campus-title">NORTH BROOKVALE CAMPUS</h2>
  <p class="sign__text campus-tagline">HOME TO THE SOCIAL CLUB</p>
  <p class="sign__text club-web">WWW.TAILWINDFIELDS.CA</p>
</section>

</body>
</html>
```